Hi Designers,

I will need 4 web pages designed. The web page looks like an App (if you click on the logo, or the icon on an iPad, it will take you to the website), but it is still a webpage.

Please check the attachment on this brief to understand what specific pages I need to be designed.

A .PSD (straight-up PhotoShop image) as final deliverable is fine, as long as you give us the exact “web color numbers”.

The design is for desktop and iPad but in a single unified web application, NOT separate web app and (native) iPad app.

Details:

Bright Harbor Policy Systems is developing a browser-based application for use on any mobile device or desktop. The app will be used by corporations to communicate with their employees regarding legal, regulatory and company requirements for conducting business. The app is known as “Workplace Guidance Hub.” When the user clicks on the icon for Workplace Guidance Hub, they will enter a site full of information that a company deems necessary for the employee to do his/her job. There are several content sections within the site, including a login page, training, policies, forms, news feeds and blogs.

The application has been built using Microsoft .NET, and fully supports CSS-type skinning; it uses traditional page layouts. We are seeking a product logo concept (image), a master application/desktop icon (image), as well as a full color scheme/theme/skin design for all areas of the application (header area, body text, menu bar, etc.) in the form of a CSS. The look should be clean, crisp and professional; nothing cartoony or whimsical. It should be easy to read and “airy”.

We have sketched prototypes for the basic application page layout that we can send as a next step of the process.
Updates

Screen shots have been uploaded to this project.  Please use them to guide your design.

Dear designers,

I apologize for the delay in providing feedback. My partners and I will provide feedback in a few days. Thank you for your patience.

Industry/Entity Type

Business

Font styles to use
Other font styles liked:
• see font on screen shots when uploaded

```html
<!DOCTYPE html>
<html lang="en">
<head>
<meta charset="utf-8">
<title>User Login – Workplace Guidance Hub</title>
<link rel="stylesheet" href="https://fonts.googleapis.com/css2?family=Source+Sans+3:wght@300;400;600;700&display=swap">
<style>
  :root {
    --page-top: #0891d2;
    --page-bottom: #0457b0;
    --footer-bg: #064a8f;
    --footer-line: #04356a;
    --footer-text: #6f9ccc;
    --sheet: #ffffff;
    --client-navy: #133a63;
    --login-top: #0a6fc2;
    --login-head-bottom: #073f86;
    --login-body-top: #0a74bb;
    --login-body-bottom: #053f7f;
    --login-text: #ffffff;
    --login-sub: #cfe2f5;
    --field-top: #ffffff;
    --field-bottom: #e6e6e6;
    --field-text: #555555;
    --button-top: #ffd21f;
    --button-bottom: #f2a900;
    --button-text: #3a2a00;
    --brand-blue: #1565c0;
  }
  * { box-sizing: border-box; margin: 0; padding: 0; }
  html, body {
    width: 1200px; height: 922px; overflow: hidden;
    font-family: "Source Sans 3", "Segoe UI", sans-serif;
  }
  .page {
    position: relative; width: 1200px; height: 922px;
    background: linear-gradient(180deg, var(--page-top) 0%, var(--page-bottom) 92%);
  }
  .sheet {
    position: absolute; left: 141px; top: 100px; width: 918px; height: 671px;
    background: var(--sheet); border-radius: 4px;
  }
  .client-name {
    position: absolute; left: 0; right: 0; top: 160px;
    display: flex; align-items: center; justify-content: center; gap: 12px;
    font-size: 24px; font-weight: 600; color: var(--client-navy);
  }
  .client-name .dot {
    width: 18px; height: 18px; border-radius: 50%; background: var(--client-navy);
  }
  .login {
    position: absolute; left: 408px; top: 249px; width: 373px; height: 347px;
    border-radius: 2px; overflow: hidden;
    background: linear-gradient(180deg, var(--login-body-top) 0%, var(--login-body-bottom) 100%);
    color: var(--login-text);
  }
  .login-head {
    height: 82px; padding: 18px 34px 0;
    background: linear-gradient(180deg, var(--login-top) 0%, var(--login-head-bottom) 100%);
  }
  .login-title { font-size: 29px; font-weight: 300; line-height: 32px; }
  .login-sub { font-size: 14px; font-weight: 300; color: var(--login-sub); line-height: 18px; }
  .login-form { padding: 20px 28px 0 33px; }
  .field {
    display: block; width: 313px; height: 37px; margin-bottom: 17px;
    padding: 0 14px; border: 1px solid #c9c9c9; border-radius: 2px;
    background: linear-gradient(180deg, var(--field-top), var(--field-bottom));
    font: 400 14px "Source Sans 3", sans-serif; color: var(--field-text);
    line-height: 35px;
  }
  .keep {
    display: flex; align-items: center; gap: 6px;
    font-size: 14px; font-weight: 600; margin-top: -1px;
  }
  .keep .box {
    width: 19px; height: 19px; background: #fff; border-radius: 2px;
  }
  .forgot {
    display: block; margin-top: 11px; font-size: 14px; font-weight: 300;
    color: var(--login-sub); text-decoration: none;
  }
  .sign-in {
    display: block; margin-top: 12px; width: 96px; height: 31px;
    border: 1px solid #d18f00; border-radius: 2px;
    background: linear-gradient(180deg, var(--button-top), var(--button-bottom));
    font: 400 18px "Source Sans 3", sans-serif; color: var(--button-text);
  }
  .product-name {
    position: absolute; left: 0; right: 0; top: 640px; text-align: center;
    font-size: 28px; font-weight: 600; color: var(--brand-blue);
  }
  .footer {
    position: absolute; left: 0; bottom: 0; width: 1200px; height: 72px;
    background: var(--footer-bg); border-top: 1px solid var(--footer-line);
  }
  .footer-note {
    position: absolute; left: 79px; top: 32px;
    font-size: 13px; font-weight: 300; color: var(--footer-text);
  }
</style>
</head>
<body>
<div class="page">
  <div class="sheet"></div>

  <div class="client-name"><span class="dot"></span>Corvella Labs</div>

  <section class="login">
    <header class="login-head">
      <h1 class="login-title">User Login</h1>
      <p class="login-sub">Duis tincidunt lectus quis dui viverra vestib.</p>
    </header>
    <div class="login-form">
      <div class="field">Username</div>
      <div class="field">Password</div>
      <label class="keep"><span class="box"></span>Keep me signed in</label>
      <a class="forgot" href="#">Forgot Password?</a>
      <button class="sign-in" type="button">Sign in</button>
    </div>
  </section>

  <div class="product-name">Workplace Guidance Hub</div>

  <footer class="footer">
    <p class="footer-note">© 2013 Company Name.&nbsp; All right reserved.&nbsp; Term of Use</p>
  </footer>
</div>
</body>
</html>
```